Service business needs Business Card Design

Looking to create a new business card design that is both professional and unique the can highlight the many services we offer throughout the seasons. Our tagline is "The Steadfast Touch"
Licensed & Insured: PA392617 has to be small and on the back side of the card.
On the Front:
FirstName LastName
Title
We offer the following services:
Deck Repair and Maintenance
Deck Cleaning and Staining/Painting
Power Washing/House Washing
Landscape Lighting Installation
Christmas Lighting Installation

```html
<!DOCTYPE html>
<html lang="en">
<head>
<meta charset="utf-8">
<title>Harbor Services – Business Card</title>
<link href="https://fonts.googleapis.com/css2?family=Orbitron:wght@700;800&family=Questrial&display=swap" rel="stylesheet">
<style>
  :root{
    --stage:#2e2e2e;
    --card-white:#ffffff;
    --navy:#0b4f92;
    --deep-blue:#064a8a;
    --sky:#45b8ea;
    --light-sky:#5cc8f2;
    --text-light:#ffffff;
  }
  *{box-sizing:border-box;margin:0;padding:0}
  html,body{width:1200px;height:689px;overflow:hidden;background:var(--stage)}
  .canvas{position:relative;width:1200px;height:689px;display:flex;align-items:center;justify-content:center;gap:40px}
  .card{position:relative;width:540px;height:309px;border-radius:22px;overflow:hidden}

  /* Back: brand side */
  .card--brand{background:var(--card-white);display:flex;flex-direction:column;align-items:center;justify-content:center;gap:34px}
  .brand-lockup{display:flex;align-items:center;gap:14px}
  .brand-dot{width:34px;height:34px;border-radius:50%;background:var(--navy)}
  .brand-name{font-family:'Orbitron',sans-serif;font-weight:800;font-size:44px;letter-spacing:2px;color:var(--navy);text-transform:uppercase;line-height:1}
  .tagline{font-family:'Orbitron',sans-serif;font-weight:800;font-size:27px;color:var(--navy);text-transform:uppercase;letter-spacing:0.5px}
  .tagline .accent{color:var(--sky)}

  /* Front: contact side */
  .card--contact{background:var(--deep-blue)}
  .burst{position:absolute;inset:0;background:radial-gradient(ellipse 75% 90% at 12% 62%, var(--light-sky) 0%, #2a8fd0 22%, #0f5fa3 48%, var(--deep-blue) 75%)}
  .contact{position:absolute;right:30px;top:34px;text-align:right;color:var(--text-light)}
  .person-name{font-family:'Orbitron',sans-serif;font-weight:800;font-size:26px;letter-spacing:1px;text-transform:uppercase;line-height:1.1}
  .person-title{font-family:'Questrial',sans-serif;font-size:16px;color:var(--sky);margin-bottom:14px}
  .services{list-style:none;font-family:'Questrial',sans-serif;font-size:14.5px;line-height:1.55}
  .services li{display:flex;align-items:center;justify-content:flex-end;gap:8px}
  .tick{width:11px;height:11px;flex:none}
  .licence{font-family:'Questrial',sans-serif;font-size:10.5px;margin-top:12px}
</style>
</head>
<body>
<main class="canvas">
  <section class="card card--brand">
    <div class="brand-lockup">
      <span class="brand-dot"></span>
      <span class="brand-name">Harbor Services</span>
    </div>
    <p class="tagline">The <span class="accent">Steadfast</span> Touch</p>
  </section>

  <section class="card card--contact">
    <div class="burst" role="img" aria-label="Soft light-blue radiant glow across the card"></div>
    <div class="contact">
      <h1 class="person-name">Daniel Reyes</h1>
      <p class="person-title">Founder &amp; CEO</p>
      <ul class="services">
        <li>Deck Repair &amp; Maintenance <svg class="tick" viewBox="0 0 12 12"><circle cx="6" cy="6" r="6" fill="#45b8ea"/><path d="M3.2 6.2l1.8 1.8 3.8-4" stroke="#fff" stroke-width="1.5" fill="none"/></svg></li>
        <li>Deck Cleaning &amp; Staining/Painting <svg class="tick" viewBox="0 0 12 12"><circle cx="6" cy="6" r="6" fill="#45b8ea"/><path d="M3.2 6.2l1.8 1.8 3.8-4" stroke="#fff" stroke-width="1.5" fill="none"/></svg></li>
        <li>Power Washing/House Washing <svg class="tick" viewBox="0 0 12 12"><circle cx="6" cy="6" r="6" fill="#45b8ea"/><path d="M3.2 6.2l1.8 1.8 3.8-4" stroke="#fff" stroke-width="1.5" fill="none"/></svg></li>
        <li>Landscape Lighting Installation <svg class="tick" viewBox="0 0 12 12"><circle cx="6" cy="6" r="6" fill="#45b8ea"/><path d="M3.2 6.2l1.8 1.8 3.8-4" stroke="#fff" stroke-width="1.5" fill="none"/></svg></li>
        <li>Christmas Lighting Installation <svg class="tick" viewBox="0 0 12 12"><circle cx="6" cy="6" r="6" fill="#45b8ea"/><path d="M3.2 6.2l1.8 1.8 3.8-4" stroke="#fff" stroke-width="1.5" fill="none"/></svg></li>
      </ul>
      <p class="licence">Licensed &amp; Insured: PA392617</p>
    </div>
  </section>
</main>
</body>
</html>
```